Simple graphic for a book or slide presentation

We are looking for a style that suits the style of our book. It's title is Harbor. Keeping a calm course through stormy seas. There will be more line drawing/graphics in the book but how you design this image will create the style for all the other simple graphics in the book (once we decide what they are). So this one design will lead to a few more to match the style of this one. We'd like the shape of the overall graphic (i.e the arrows and words/bubbles) to be circular (not a rounded square as appears in the sample attached). Perhaps the words don't need to be in ovals or bound by anything at all; perhaps they do - let's see what you see. We'd like you to choose a font or offer many different fonts you think will capture the practical yet unconventional tone of the book. The book is teaching that managing risks in life is a life-skill that can be learned. The section of the book where this graphic will be placed is called "the power of language" - basically we are saying that thoughts, words and actions create our culture and our destiny. This insight comes from Torvel Pelloru's famous quote:
Carefully watch your thoughts, for they become your words.
Manage and watch your words, for they will become your actions.
Consider and judge your actions, for they have become your habits.
Acknowledge and watch your habits, for they shall become your values.
Understand and embrace your values, for they become your destiny.

Please change the text in the middle of the graphic to say: The Human Culture Cycle

```html
<!DOCTYPE html>
<html lang="en">
<head>
<meta charset="utf-8">
<title>The Human Culture Cycle</title>
<link rel="stylesheet" href="https://fonts.googleapis.com/css2?family=Open+Sans:wght@700;800&display=swap">
<style>
  :root {
    --canvas: #ffffff;
    --gap: #ffffff;
    --thoughts: #5159a8;
    --words: #7794cb;
    --actions: #06cc9c;
    --habits: #7ee418;
    --values: #16a0c2;
    --culture: #02717d;
    --label: #ffffff;
    --title: #767676;
  }
  html, body {
    margin: 0;
    padding: 0;
    width: 1200px;
    height: 1000px;
    overflow: hidden;
    background: var(--canvas);
  }
  .cycle-graphic {
    position: relative;
    width: 1200px;
    height: 1000px;
  }
  .cycle-ring {
    position: absolute;
    inset: 0;
    width: 1200px;
    height: 1000px;
  }
  .segment {
    stroke: var(--gap);
    stroke-width: 18;
    stroke-linejoin: miter;
  }
  .segment--thoughts { fill: var(--thoughts); }
  .segment--words { fill: var(--words); }
  .segment--actions { fill: var(--actions); }
  .segment--habits { fill: var(--habits); }
  .segment--values { fill: var(--values); }
  .segment--culture { fill: var(--culture); }
  .inner-glow {
    fill: none;
    stroke: var(--gap);
    stroke-opacity: 0.3;
    stroke-width: 80;
  }
  .stage-label {
    fill: var(--label);
    font-family: "Open Sans", sans-serif;
    font-weight: 700;
    font-size: 80px;
    letter-spacing: 3px;
  }
  .cycle-title {
    position: absolute;
    left: 0;
    width: 1200px;
    top: 330px;
    margin: 0;
    text-align: center;
    font-family: "Open Sans", sans-serif;
    font-weight: 800;
    font-size: 60px;
    line-height: 80px;
    color: var(--title);
    letter-spacing: 1px;
  }
  .cycle-title span { display: block; }
</style>
</head>
<body>
<main class="cycle-graphic">
  <svg class="cycle-ring" viewBox="0 0 2100 1750" aria-hidden="true">
    <defs>
      <path id="label-track" pathLength="720"
        d="M1050,363 A512,512 0 1 1 1050,1387 A512,512 0 1 1 1050,363 A512,512 0 1 1 1050,1387 A512,512 0 1 1 1050,363"/>
    </defs>

    <path class="segment segment--thoughts" d="M725,312.1 A650,650 0 0 1 1375,312.1 L1408,477.4 L1260,511.3 A420,420 0 0 0 840,511.3 L884.7,366.2 Z"/>
    <path class="segment segment--words" d="M1375,312.1 A650,650 0 0 1 1700,875 L1573.3,986.2 L1470,875 A420,420 0 0 0 1260,511.3 L1408,477.4 Z"/>
    <path class="segment segment--actions" d="M1700,875 A650,650 0 0 1 1375,1437.9 L1215.3,1383.8 L1260,1238.7 A420,420 0 0 0 1470,875 L1573.3,986.2 Z"/>
    <path class="segment segment--habits" d="M1375,1437.9 A650,650 0 0 1 725,1437.9 L692,1272.6 L840,1238.7 A420,420 0 0 0 1260,1238.7 L1215.3,1383.8 Z"/>
    <path class="segment segment--values" d="M725,1437.9 A650,650 0 0 1 400,875 L526.7,763.8 L630,875 A420,420 0 0 0 840,1238.7 L692,1272.6 Z"/>
    <path class="segment segment--culture" d="M400,875 A650,650 0 0 1 725,312.1 L884.7,366.2 L840,511.3 A420,420 0 0 0 630,875 L526.7,763.8 Z"/>

    <circle class="inner-glow" cx="1050" cy="875" r="460"/>

    <text class="stage-label"><textPath href="#label-track" startOffset="369" text-anchor="middle">THOUGHTS</textPath></text>
    <text class="stage-label"><textPath href="#label-track" startOffset="429" text-anchor="middle">WORDS</textPath></text>
    <text class="stage-label"><textPath href="#label-track" startOffset="489" text-anchor="middle">ACTIONS</textPath></text>
    <text class="stage-label"><textPath href="#label-track" startOffset="549" text-anchor="middle">HABITS</textPath></text>
    <text class="stage-label"><textPath href="#label-track" startOffset="609" text-anchor="middle">VALUES</textPath></text>
    <text class="stage-label"><textPath href="#label-track" startOffset="669" text-anchor="middle">CULTURE</textPath></text>
  </svg>

  <h1 class="cycle-title">
    <span>THE</span>
    <span>HUMAN</span>
    <span>CULTURE</span>
    <span>CYCLE</span>
  </h1>
</main>
</body>
</html>
```